Tarvel Works - Powerpoint Templates

We are a consultancy to help builders to optimize their planning in order to save building costs. For that reason we need templates for teasers and presentations where we offer our services, show our team and their capacities and present workflows, organization charts, price lists etc.

```html
<!DOCTYPE html>
<html lang="en">
<head>
<meta charset="utf-8">
<title>Tarvel Works – Presentation Templates</title>
<link rel="stylesheet" href="https://fonts.googleapis.com/css2?family=Orbitron:wght@600;700&family=Montserrat:wght@400;500;600;700&display=swap">
<style>
:root{
  --gold:#c4872c;
  --gold-deep:#b8791f;
  --gold-light:#f0c862;
  --gold-soft:#e3b04f;
  --ink:#2f2f35;
  --text:#555559;
  --muted:#8a8a8e;
  --line:#e4e4e4;
  --stage:#d9dbe0;
  --board:#c8c8c8;
  --white:#ffffff;
}
*{box-sizing:border-box;margin:0;padding:0}
html,body{width:1200px;height:2742px;overflow:hidden}
body{background:var(--board);font-family:"Montserrat",Arial,sans-serif;color:var(--text)}
.canvas{position:relative;width:1200px;height:2742px;overflow:hidden;background:var(--board)}
.stage{position:absolute;left:0;top:0;width:1200px;height:700px;background:linear-gradient(180deg,#cfd3da 0%,#e4e5e8 100%)}
.stage-brand{position:absolute;right:52px;top:118px;display:flex;align-items:center;gap:12px;font:700 26px "Orbitron",sans-serif;color:var(--gold);letter-spacing:1px}
.stage-brand .dot{width:26px;height:26px;background:var(--gold)}
.feature{position:absolute;left:233px;top:150px;transform:scale(1.3);transform-origin:0 0;box-shadow:0 18px 40px rgba(0,0,0,.18)}

.slide{position:absolute;width:563px;height:316px;background:var(--white);overflow:hidden}
.slide > *{position:absolute}
.col-l{left:28px}.col-r{left:609px}
.row1{top:718px}.row2{top:1054px}.row3{top:1389px}.row4{top:1724px}.row5{top:2059px}.row6{top:2395px}

.brand{display:flex;align-items:center;gap:6px;font:700 13px "Orbitron",sans-serif;color:var(--gold);letter-spacing:.5px}
.brand .dot{width:13px;height:13px;background:var(--gold)}
.brand-sm{left:14px;bottom:12px;display:flex;align-items:center;gap:4px;font:700 7.5px "Orbitron",sans-serif;color:var(--gold)}
.brand-sm .dot{width:8px;height:8px;background:var(--gold)}
.copy{right:32px;bottom:14px;font-size:4.5px;letter-spacing:.2px;color:var(--ink);text-transform:uppercase}
.pg{right:14px;bottom:12px;width:9px;height:9px;background:var(--gold);color:#fff;font:700 5px "Montserrat",sans-serif;display:flex;align-items:center;justify-content:center}
.s-title{top:22px;left:0;width:100%;text-align:center;font:700 18px "Orbitron",sans-serif;letter-spacing:2.5px;color:var(--ink)}
.lorem{font-size:6px;line-height:7.2px;color:var(--text)}
.h-gold{font:600 9px "Montserrat",sans-serif;color:var(--gold)}
.h-ink{font:700 8.5px "Montserrat",sans-serif;color:var(--ink)}

/* cover */
.cover-art{left:0;top:0;width:563px;height:316px}
.cover .brand{left:34px;top:38px}
.cover-kicker{left:34px;top:118px;font:700 19px "Orbitron",sans-serif;color:var(--gold);letter-spacing:.5px}
.cover-title{left:34px;top:140px;font:700 16px "Orbitron",sans-serif;color:var(--ink);letter-spacing:1px}
.cover .lorem{left:34px;top:170px;width:196px}
.cover-date{left:34px;top:225px;font-size:6px;color:var(--ink)}
.cover-copy{left:34px;top:275px;font-size:4.5px;color:var(--ink);text-transform:uppercase}

/* team */
.member{top:73px;width:140px;text-align:center}
.avatar{width:98px;height:98px;margin:0 auto;border-radius:50%;border:2px solid var(--gold-light);background:radial-gradient(circle at 50% 40%,#e9e7e4,#9b9896)}
.member .h-gold{margin-top:10px}
.member .job{font-size:5.5px;color:var(--ink);margin-top:2px}
.member .lorem{margin-top:9px}

/* photo cards */
.band{left:0;top:0;width:563px;height:108px;background:linear-gradient(90deg,#b9812c,#d9a654 50%,#b57c27)}
.band-title{top:26px;left:0;width:100%;text-align:center;font:700 18px "Orbitron",sans-serif;letter-spacing:2.5px;color:#fff}
.card{top:72px;width:118px}
.card-img{height:70px}
.card .h-gold{margin-top:12px}
.card .lorem{margin-top:6px}

/* icon columns */
.feat{top:66px;width:110px}
.icon{width:40px;height:40px;border-radius:50%;margin:0 auto;display:flex;align-items:center;justify-content:center}
.feat .h-ink{margin-top:14px;text-align:center}
.feat .lorem{margin-top:4px;text-align:center}
.feat ul{margin-top:12px;list-style:none;font-size:5px;line-height:11.5px;color:var(--ink)}
.feat li::before{content:"";display:inline-block;width:2.5px;height:2.5px;border-radius:50%;background:var(--gold);margin:0 5px 1px 0}
.divider{top:108px;width:1px;height:150px;background:var(--line)}

/* timeline */
.step{top:116px;width:84px;text-align:center}
.num{width:26px;height:26px;border-radius:50%;margin:0 auto;color:#fff;font:700 13px "Montserrat",sans-serif;display:flex;align-items:center;justify-content:center;box-shadow:0 0 0 3px #fff,0 0 0 4px var(--line)}
.step .lorem{margin-top:14px}

/* text blocks */
.block{width:150px}
.block.right-al{text-align:right}

.pct-label{top:210px;width:130px;text-align:center}
.pct-label .lorem{margin-top:6px}

/* table */
.data{left:28px;top:75px;width:505px;border-collapse:collapse;font-size:5.5px;color:var(--ink)}
.data th{height:25px;background:var(--gold);color:#fff;font-weight:600;font-size:5.5px;line-height:6.5px}
.data th:first-child{background:#4b4b50;text-align:left;padding-left:6px}
.data th.hl{background:var(--gold-light);color:var(--ink)}
.data td{height:23px;text-align:center;border-bottom:1px solid #ececec}
.data td:first-child{text-align:left;padding-left:6px;font-weight:600}
.data td.hl{font-weight:700}
.hl-frame{left:185px;top:68px;width:87px;height:196px;border:1.5px solid var(--gold-light);border-radius:4px}

/* contact */
.contact .brand{left:34px;top:140px}
.contact-head{left:40px;top:178px;font:600 10px "Montserrat",sans-serif;color:var(--ink)}
.contact-list{left:40px;top:200px;list-style:none;font-size:6.5px;color:var(--ink);line-height:15.5px}
.contact-list li{display:flex;align-items:center;gap:8px}
.contact-list svg{width:8px;height:8px}
</style>
</head>
<body>
<div class="canvas">

  <section class="stage" aria-label="Cover preview">
    <div class="stage-brand"><span class="dot"></span>TARVEL WORKS</div>
  </section>

  <!-- cover slide, featured -->
  <article class="slide cover feature">
    <svg class="cover-art" viewBox="0 0 563 316" role="img" aria-label="Photo: two people looking up at a modern building facade">
      <defs>
        <linearGradient id="goldA" x1="0" y1="1" x2="1" y2="0"><stop offset="0" stop-color="#b9791f"/><stop offset="1" stop-color="#f2ca66"/></linearGradient>
        <linearGradient id="photoA" x1="0" y1="0" x2="1" y2="1"><stop offset="0" stop-color="#bfc7cf"/><stop offset=".55" stop-color="#7d8791"/><stop offset="1" stop-color="#2d3440"/></linearGradient>
      </defs>
      <path d="M310 0H563V316H330C290 250 250 170 240 115C230 55 262 0 310 0Z" fill="url(#goldA)"/>
      <path d="M395 0H563V316H405C370 255 330 185 318 135C305 75 340 18 395 0Z" fill="url(#photoA)"/>
    </svg>
    <div class="brand"><span class="dot"></span>TARVEL WORKS</div>
    <div class="cover-kicker">PRESENTATION</div>
    <div class="cover-title">HEADING HERE</div>
    <p class="lorem">Lorem ipsum dolor sit amet, consectetur adipiscing elit. Vivamus eu dui ex. Curabitur dapibus dignissim dui, in molestie metus feugiat sed. Praesent aliquet lorem ex.</p>
    <div class="cover-date">Saturday, July 8, 2023</div>
    <div class="cover-copy">Copyright © 2023 Tarvel Works. All rights reserved.</div>
  </article>

  <!-- row 1: covers -->
  <article class="slide cover col-l row1">
    <svg class="cover-art" viewBox="0 0 563 316" role="img" aria-label="Photo: two people looking up at a modern building facade">
      <defs>
        <linearGradient id="goldB" x1="0" y1="1" x2="1" y2="0"><stop offset="0" stop-color="#b9791f"/><stop offset="1" stop-color="#f2ca66"/></linearGradient>
        <linearGradient id="photoB" x1="0" y1="0" x2="1" y2="1"><stop offset="0" stop-color="#bfc7cf"/><stop offset=".55" stop-color="#7d8791"/><stop offset="1" stop-color="#2d3440"/></linearGradient>
      </defs>
      <path d="M310 0H563V316H330C290 250 250 170 240 115C230 55 262 0 310 0Z" fill="url(#goldB)"/>
      <path d="M395 0H563V316H405C370 255 330 185 318 135C305 75 340 18 395 0Z" fill="url(#photoB)"/>
    </svg>
    <div class="brand"><span class="dot"></span>TARVEL WORKS</div>
    <div class="cover-kicker">PRESENTATION</div>
    <div class="cover-title">HEADING HERE</div>
    <p class="lorem">Lorem ipsum dolor sit amet, consectetur adipiscing elit. Vivamus eu dui ex. Curabitur dapibus dignissim dui, in molestie metus feugiat sed. Praesent aliquet lorem ex.</p>
    <div class="cover-date">Saturday, July 8, 2023</div>
    <div class="cover-copy">Copyright © 2023 Tarvel Works. All rights reserved.</div>
  </article>

  <article class="slide cover col-r row1">
    <svg class="cover-art" viewBox="0 0 563 316" role="img" aria-label="Photo: handshake over a tablet showing a stock chart">
      <defs>
        <linearGradient id="goldC" x1="0" y1="1" x2="1" y2="0"><stop offset="0" stop-color="#b9791f"/><stop offset="1" stop-color="#f2ca66"/></linearGradient>
        <linearGradient id="photoC" x1="1" y1="0" x2="0" y2="1"><stop offset="0" stop-color="#c9d3dc"/><stop offset=".5" stop-color="#6f7c8a"/><stop offset="1" stop-color="#1f2833"/></linearGradient>
      </defs>
      <path d="M310 0H563V316H330C290 250 250 170 240 115C230 55 262 0 310 0Z" fill="url(#goldC)"/>
      <path d="M395 0H563V316H405C370 255 330 185 318 135C305 75 340 18 395 0Z" fill="url(#photoC)"/>
    </svg>
    <div class="brand"><span class="dot"></span>TARVEL WORKS</div>
    <div class="cover-kicker">PRESENTATION</div>
    <div class="cover-title">HEADING HERE</div>
    <p class="lorem">Lorem ipsum dolor sit amet, consectetur adipiscing elit. Vivamus eu dui ex. Curabitur dapibus dignissim dui, in molestie metus feugiat sed. Praesent aliquet lorem ex.</p>
    <div class="cover-date">Saturday, July 8, 2023</div>
    <div class="cover-copy">Copyright © 2023 Tarvel Works. All rights reserved.</div>
  </article>

  <!-- row 2 -->
  <article class="slide col-l row2">
    <h2 class="s-title">MEET OUR TEAM</h2>
    <div class="member" style="left:46px">
      <div class="avatar" role="img" aria-label="Team member portrait"></div>
      <div class="h-gold">Name Goes Here</div><div class="job">Job Title Goes Here</div>
      <p class="lorem">Lorem ipsum dolor sit amet, consectetur adipiscing elit. Vivamus eu dui ex. Curabitur dapibus dignissim dui, in molestie metus feugiat sed. Praesent aliquet lorem ex, eu dapibus odio varius at.</p>
    </div>
    <div class="member" style="left:212px">
      <div class="avatar" role="img" aria-label="Team member portrait"></div>
      <div class="h-gold">Name Goes Here</div><div class="job">Job Title Goes Here</div>
      <p class="lorem">Lorem ipsum dolor sit amet, consectetur adipiscing elit. Vivamus eu dui ex. Curabitur dapibus dignissim dui, in molestie metus feugiat sed. Praesent aliquet lorem ex, eu dapibus odio varius at.</p>
    </div>
    <div class="member" style="left:377px">
      <div class="avatar" role="img" aria-label="Team member portrait"></div>
      <div class="h-gold">Name Goes Here</div><div class="job">Job Title Goes Here</div>
      <p class="lorem">Lorem ipsum dolor sit amet, consectetur adipiscing elit. Vivamus eu dui ex. Curabitur dapibus dignissim dui, in molestie metus feugiat sed. Praesent aliquet lorem ex, eu dapibus odio varius at.</p>
    </div>
    <div class="brand-sm"><span class="dot"></span>TARVEL WORKS</div>
    <div class="copy">Copyright © 2023 Tarvel Works. All rights reserved.</div>
    <div class="pg">3</div>
  </article>

  <article class="slide col-r row2">
    <div class="band" role="img" aria-label="Gold-toned photo of a building facade"></div>
    <h2 class="band-title">HEADING GOES HERE</h2>
    <div class="card" style="left:32px"><div class="card-img" role="img" aria-label="Photo: business handshake" style="background:linear-gradient(135deg,#5d6e82,#2b3340)"></div><div class="h-gold">Heading Goes Here</div><p class="lorem">Lorem ipsum dolor sit amet, consectetur adipiscing elit. Vivamus eu dui ex. Curabitur dapibus dignissim dui, in molestie metus feugiat sed. Praesent aliquet lorem ex, eu dapibus odio varius at. Duis eget tellus porta, consequat lacus vitae, venenatis dolor. Nulla facilisi.</p></div>
    <div class="card" style="left:160px"><div class="card-img" role="img" aria-label="Photo: team reviewing charts at a desk" style="background:linear-gradient(135deg,#c9a883,#7b6a5a)"></div><div class="h-gold">Heading Goes Here</div><p class="lorem">Lorem ipsum dolor sit amet, consectetur adipiscing elit. Vivamus eu dui ex. Curabitur dapibus dignissim dui, in molestie metus feugiat sed. Praesent aliquet lorem ex, eu dapibus odio varius at. Duis eget tellus porta, consequat lacus vitae, venenatis dolor. Nulla facilisi.</p></div>
    <div class="card" style="left:288px"><div class="card-img" role="img" aria-label="Photo: hand pointing at printed charts" style="background:linear-gradient(135deg,#eef1f6,#a9b7cc)"></div><div class="h-gold">Heading Goes Here</div><p class="lorem">Lorem ipsum dolor sit amet, consectetur adipiscing elit. Vivamus eu dui ex. Curabitur dapibus dignissim dui, in molestie metus feugiat sed. Praesent aliquet lorem ex, eu dapibus odio varius at. Duis eget tellus porta, consequat lacus vitae, venenatis dolor. Nulla facilisi.</p></div>
    <div class="card" style="left:416px"><div class="card-img" role="img" aria-label="Photo: overhead view of a planning meeting" style="background:linear-gradient(135deg,#d9c7ad,#8f7a63)"></div><div class="h-gold">Heading Goes Here</div><p class="lorem">Lorem ipsum dolor sit amet, consectetur adipiscing elit. Vivamus eu dui ex. Curabitur dapibus dignissim dui, in molestie metus feugiat sed. Praesent aliquet lorem ex, eu dapibus odio varius at. Duis eget tellus porta, consequat lacus vitae, venenatis dolor. Nulla facilisi.</p></div>
    <div class="brand-sm"><span class="dot"></span>TARVEL WORKS</div>
    <div class="copy">Copyright © 2023 Tarvel Works. All rights reserved.</div>
    <div class="pg">4</div>
  </article>

  <!-- row 3 -->
  <article class="slide col-l row3">
    <h2 class="s-title">HEADING GOES HERE</h2>
    <div class="divider" style="left:158px"></div>
    <div class="divider" style="left:281px"></div>
    <div class="divider" style="left:404px"></div>
    <div class="feat" style="left:41px">
      <div class="icon" style="background:var(--gold-deep)"><svg width="18" height="18" viewBox="0 0 18 18"><circle cx="9" cy="6" r="3.5" fill="#fff"/><path d="M2 17c0-4 3-6.5 7-6.5s7 2.5 7 6.5z" fill="#fff"/></svg></div>
      <div class="h-ink">Heading Goes Here</div>
      <p class="lorem">Lorem ipsum dolor sit amet, consectetur adipiscing elit. Vivamus eu dui ex. Curabitur dapibus dignissim dui, in molestie metus feugiat sed.</p>
      <ul><li>Lorem Ipsum Dolor Sit Amet.</li><li>Consectetur Adipiscing Elit.</li><li>Vivamus Eu Dui Ex.</li><li>Curabitur Dapibus Dignissim</li><li>Metus Feugiat Sed.</li></ul>
    </div>
    <div class="feat" style="left:164px">
      <div class="icon" style="background:var(--gold-light)"><svg width="18" height="18" viewBox="0 0 18 18"><rect x="2" y="3" width="14" height="13" rx="1.5" fill="none" stroke="#fff" stroke-width="1.6"/><path d="M2 7h14M6 10h2M10 10h2M6 13h2M10 13h2" stroke="#fff" stroke-width="1.6"/></svg></div>
      <div class="h-ink">Heading Goes Here</div>
      <p class="lorem">Lorem ipsum dolor sit amet, consectetur adipiscing elit. Vivamus eu dui ex. Curabitur dapibus dignissim dui, in molestie metus feugiat sed.</p>
      <ul><li>Lorem Ipsum Dolor Sit Amet.</li><li>Consectetur Adipiscing Elit.</li><li>Vivamus Eu Dui Ex.</li><li>Curabitur Dapibus Dignissim</li><li>Metus Feugiat Sed.</li></ul>
    </div>
    <div class="feat" style="left:287px">
      <div class="icon" style="background:var(--gold-deep)"><svg width="20" height="20" viewBox="0 0 20 20"><circle cx="10" cy="10" r="7.5" fill="none" stroke="#fff" stroke-width="1.8"/><path d="M10 5.5V10h3.5" fill="none" stroke="#fff" stroke-width="1.8"/></svg></div>
      <div class="h-ink">Heading Goes Here</div>
      <p class="lorem">Lorem ipsum dolor sit amet, consectetur adipiscing elit. Vivamus eu dui ex. Curabitur dapibus dignissim dui, in molestie metus feugiat sed.</p>
      <ul><li>Lorem Ipsum Dolor Sit Amet.</li><li>Consectetur Adipiscing Elit.</li><li>Vivamus Eu Dui Ex.</li><li>Curabitur Dapibus Dignissim</li><li>Metus Feugiat Sed.</li></ul>
    </div>
    <div class="feat" style="left:410px">
      <div class="icon" style="background:var(--gold-light)"><svg width="18" height="18" viewBox="0 0 18 18"><rect x="2" y="8" width="3.5" height="8" fill="#fff"/><path d="M7 8l3-6c1.5 0 2 1 1.6 2.5L11 7h4c1 0 1.6 1 1.3 2l-1.6 6c-.2.7-.8 1-1.4 1H7z" fill="#fff"/></svg></div>
      <div class="h-ink">Heading Goes Here</div>
      <p class="lorem">Lorem ipsum dolor sit amet, consectetur adipiscing elit. Vivamus eu dui ex. Curabitur dapibus dignissim dui, in molestie metus feugiat sed.</p>
      <ul><li>Lorem Ipsum Dolor Sit Amet.</li><li>Consectetur Adipiscing Elit.</li><li>Vivamus Eu Dui Ex.</li><li>Curabitur Dapibus Dignissim</li><li>Metus Feugiat Sed.</li></ul>
    </div>
    <div class="brand-sm"><span class="dot"></span>TARVEL WORKS</div>
    <div class="copy">Copyright © 2023 Tarvel Works. All rights reserved.</div>
    <div class="pg">5</div>
  </article>

  <article class="slide col-r row3">
    <h2 class="s-title">HEADING GOES HERE</h2>
    <svg style="left:0;top:124px" width="563" height="10" viewBox="0 0 563 10"><line x1="0" y1="5" x2="535" y2="5" stroke="#bdbdbd" stroke-width=".8" stroke-dasharray="2 2"/><path d="M533 2l4 3-4 3" fill="none" stroke="#bdbdbd" stroke-width=".8"/></svg>
    <div class="step" style="left:47px"><div class="num" style="background:var(--gold-deep)">1</div><p class="lorem">Lorem ipsum dolor sit amet, consectetur adipiscing elit. Vivamus eu dui ex. Curabitur dapibus dignissim dui, in molestie metus feugiat sed. Praesent aliquet lorem ex.</p></div>
    <div class="step" style="left:143px"><div class="num" style="background:var(--gold-light)">2</div><p class="lorem">Lorem ipsum dolor sit amet, consectetur adipiscing elit. Vivamus eu dui ex. Curabitur dapibus dignissim dui, in molestie metus feugiat sed. Praesent aliquet lorem ex.</p></div>
    <div class="step" style="left:239px"><div class="num" style="background:var(--gold-deep)">3</div><p class="lorem">Lorem ipsum dolor sit amet, consectetur adipiscing elit. Vivamus eu dui ex. Curabitur dapibus dignissim dui, in molestie metus feugiat sed. Praesent aliquet lorem ex.</p></div>
    <div class="step" style="left:335px"><div class="num" style="background:var(--gold-light)">4</div><p class="lorem">Lorem ipsum dolor sit amet, consectetur adipiscing elit. Vivamus eu dui ex. Curabitur dapibus dignissim dui, in molestie metus feugiat sed. Praesent aliquet lorem ex.</p></div>
    <div class="step" style="left:430px"><div class="num" style="background:var(--gold-deep)">5</div><p class="lorem">Lorem ipsum dolor sit amet, consectetur adipiscing elit. Vivamus eu dui ex. Curabitur dapibus dignissim dui, in molestie metus feugiat sed. Praesent aliquet lorem ex.</p></div>
    <div class="brand-sm"><span class="dot"></span>TARVEL WORKS</div>
    <div class="copy">Copyright © 2023 Tarvel Works. All rights reserved.</div>
    <div class="pg">6</div>
  </article>

  <!-- row 4 -->
  <article class="slide col-l row4">
    <h2 class="s-title">HEADING GOES HERE</h2>
    <svg style="left:197px;top:81px" width="168" height="168" viewBox="-84 -84 168 168">
      <path d="M0-82A82 82 0 0 0-82 0H-46A46 46 0 0 1 0-46Z" fill="var(--gold-deep)"/>
      <path d="M0-82A82 82 0 0 1 82 0H46A46 46 0 0 0 0-46Z" fill="var(--gold-light)"/>
      <path d="M82 0A82 82 0 0 1 0 82V46A46 46 0 0 0 46 0Z" fill="var(--gold-deep)"/>
      <path d="M0 82A82 82 0 0 1-82 0H-46A46 46 0 0 0 0 46Z" fill="var(--gold-light)"/>
      <path d="M0-84V84M-84 0H84" stroke="#fff" stroke-width="3"/>
      <circle r="38" fill="none" stroke="#e6e6e6" stroke-width="7"/>
      <circle r="14" fill="var(--gold)"/>
      <g fill="#fff"><circle cx="-46" cy="-53" r="10"/><circle cx="53" cy="-46" r="10"/><circle cx="53" cy="46" r="10"/><circle cx="-46" cy="53" r="10"/></g>
      <circle cx="53" cy="-47" r="4" fill="none" stroke="var(--gold-deep)" stroke-width="1.5"/><path d="M56 -44l3 3" stroke="var(--gold-deep)" stroke-width="1.5"/>
      <circle cx="-46" cy="-54" r="4" fill="var(--gold-light)"/><rect x="-48" y="-50" width="4" height="3" fill="var(--gold-light)"/>
      <path d="M-51 57h3v-4h3v4h3v-8h3v8" fill="none" stroke="var(--gold-light)" stroke-width="1.5"/>
      <circle cx="49" cy="45" r="2.5" fill="var(--gold-deep)"/><circle cx="57" cy="45" r="2.5" fill="var(--gold-deep)"/><path d="M45 51c1-3 7-3 8 0M53 51c1-3 7-3 8 0" fill="none" stroke="var(--gold-deep)" stroke-width="1.5"/>
    </svg>
    <div class="block right-al" style="left:32px;top:83px"><div class="h-gold" style="color:var(--gold-light)">Heading Goes Here</div><p class="lorem" style="margin-top:5px">Lorem ipsum dolor sit amet, consectetur adipiscing elit. Vivamus eu dui ex. Curabitur dapibus dignissim dui, in molestie metus feugiat sed. Praesent aliquet lorem ex.</p></div>
    <div class="block right-al" style="left:32px;top:194px"><div class="h-gold">Heading Goes Here</div><p class="lorem" style="margin-top:5px">Lorem ipsum dolor sit amet, consectetur adipiscing elit. Vivamus eu dui ex. Curabitur dapibus dignissim dui, in molestie metus feugiat sed. Praesent aliquet lorem ex.</p></div>
    <div class="block" style="left:379px;top:83px"><div class="h-gold">Heading Goes Here</div><p class="lorem" style="margin-top:5px">Lorem ipsum dolor sit amet, consectetur adipiscing elit. Vivamus eu dui ex. Curabitur dapibus dignissim dui, in molestie metus feugiat sed. Praesent aliquet lorem ex.</p></div>
    <div class="block" style="left:379px;top:194px"><div class="h-gold" style="color:var(--gold-light)">Heading Goes Here</div><p class="lorem" style="margin-top:5px">Lorem ipsum dolor sit amet, consectetur adipiscing elit. Vivamus eu dui ex. Curabitur dapibus dignissim dui, in molestie metus feugiat sed. Praesent aliquet lorem ex.</p></div>
    <div class="brand-sm"><span class="dot"></span>TARVEL WORKS</div>
    <div class="copy">Copyright © 2023 Tarvel Works. All rights reserved.</div>
    <div class="pg">7</div>
  </article>

  <article class="slide col-r row4">
    <h2 class="s-title">HEADING GOES HERE</h2>
    <svg style="left:40px;top:86px" width="230" height="100" viewBox="0 0 230 100" font-family="Montserrat,sans-serif" font-size="5" fill="#555">
      <text x="0" y="10">Category 4</text><text x="0" y="32">Category 3</text><text x="0" y="54">Category 2</text><text x="0" y="76">Category 1</text>
      <g transform="translate(40,0)">
        <rect x="0" y="5" width="28" height="8" fill="var(--gold-deep)"/><rect x="28" y="5" width="36" height="8" fill="var(--gold-light)"/><rect x="64" y="5" width="62" height="8" fill="var(--ink)"/>
        <rect x="0" y="27" width="44" height="8" fill="var(--gold-deep)"/><rect x="44" y="27" width="22" height="8" fill="var(--gold-light)"/><rect x="66" y="27" width="36" height="8" fill="var(--ink)"/>
        <rect x="0" y="49" width="31" height="8" fill="var(--gold-deep)"/><rect x="31" y="49" width="56" height="8" fill="var(--gold-light)"/><rect x="87" y="49" width="25" height="8" fill="var(--ink)"/>
        <rect x="0" y="71" width="53" height="8" fill="var(--gold-deep)"/><rect x="53" y="71" width="31" height="8" fill="var(--gold-light)"/><rect x="84" y="71" width="25" height="8" fill="var(--ink)"/>
        <g text-anchor="middle"><text x="0" y="98">0</text><text x="25" y="98">2</text><text x="50" y="98">4</text><text x="75" y="98">6</text><text x="100" y="98">8</text><text x="125" y="98">10</text><text x="150" y="98">12</text><text x="175" y="98">14</text></g>
      </g>
    </svg>
    <svg style="left:290px;top:82px" width="230" height="115" viewBox="0 0 230 115" font-family="Montserrat,sans-serif" font-size="5" fill="#555">
      <g text-anchor="end"><text x="8" y="6">10</text><text x="8" y="15">9</text><text x="8" y="24">8</text><text x="8" y="33">7</text><text x="8" y="42">6</text><text x="8" y="51">5</text><text x="8" y="60">4</text><text x="8" y="69">3</text><text x="8" y="78">2</text><text x="8" y="87">1</text><text x="8" y="96">0</text></g>
      <line x1="12" y1="94" x2="230" y2="94" stroke="#ccc" stroke-width=".6"/>
      <g transform="translate(12,0)">
        <rect x="8" y="18" width="10" height="76" fill="var(--gold-deep)"/><rect x="19" y="40" width="10" height="54" fill="var(--gold-light)"/><rect x="30" y="73" width="10" height="21" fill="var(--ink)"/>
        <rect x="62" y="31" width="10" height="63" fill="var(--gold-deep)"/><rect x="73" y="44" width="10" height="50" fill="var(--gold-light)"/><rect x="84" y="74" width="10" height="20" fill="var(--ink)"/>
        <rect x="116" y="40" width="10" height="54" fill="var(--gold-deep)"/><rect x="127" y="11" width="10" height="83" fill="var(--gold-light)"/><rect x="138" y="63" width="10" height="31" fill="var(--ink)"/>
        <rect x="170" y="53" width="10" height="41" fill="var(--gold-deep)"/><rect x="181" y="69" width="10" height="25" fill="var(--gold-light)"/><rect x="192" y="49" width="10" height="45" fill="var(--ink)"/>
        <g text-anchor="middle"><text x="24" y="104">Category 1</text><text x="78" y="104">Category 2</text><text x="132" y="104">Category 3</text><text x="186" y="104">Category 4</text></g>
      </g>
    </svg>
    <div class="block" style="left:45px;top:216px;width:215px"><div class="h-gold">Heading Goes Here</div><p class="lorem" style="margin-top:3px">Lorem ipsum dolor sit amet, consectetur adipiscing elit. Vivamus eu dui ex. Curabitur dapibus dignissim dui, in molestie metus feugiat sed. Praesent aliquet lorem ex.</p></div>
    <div class="block" style="left:295px;top:216px;width:215px"><div class="h-gold">Heading Goes Here</div><p class="lorem" style="margin-top:3px">Lorem ipsum dolor sit amet, consectetur adipiscing elit. Vivamus eu dui ex. Curabitur dapibus dignissim dui, in molestie metus feugiat sed. Praesent aliquet lorem ex.</p></div>
    <div class="brand-sm"><span class="dot"></span>TARVEL WORKS</div>
    <div class="copy">Copyright © 2023 Tarvel Works. All rights reserved.</div>
    <div class="pg">8</div>
  </article>

  <!-- row 5 -->
  <article class="slide col-l row5">
    <h2 class="s-title">HEADING GOES HERE</h2>
    <svg style="left:0;top:85px" width="563" height="110" viewBox="0 0 563 110" font-family="Orbitron,sans-serif" font-weight="700" font-size="17" text-anchor="middle">
      <g fill="none" stroke-width="11">
        <circle cx="124" cy="54" r="48" stroke="#e2e2e2"/>
        <circle cx="124" cy="54" r="48" stroke="var(--gold-deep)" stroke-dasharray="105.6 301.6" transform="rotate(-90 124 54)"/>
        <circle cx="281" cy="54" r="48" stroke="#e2e2e2"/>
        <circle cx="281" cy="54" r="48" stroke="var(--gold-light)" stroke-dasharray="196 301.6" transform="rotate(-90 281 54)"/>
        <circle cx="437" cy="54" r="48" stroke="#e2e2e2"/>
        <circle cx="437" cy="54" r="48" stroke="var(--ink)" stroke-dasharray="256.4 301.6" transform="rotate(-90 437 54)"/>
      </g>
      <text x="124" y="60" fill="var(--gold-deep)">35%</text>
      <text x="281" y="60" fill="var(--gold-light)">65%</text>
      <text x="437" y="60" fill="var(--ink)">85%</text>
    </svg>
    <div class="pct-label" style="left:59px"><div class="h-ink">Heading Goes Here</div><p class="lorem">Lorem ipsum dolor sit amet, consectetur adipiscing elit. Vivamus eu dui ex. Curabitur dapibus dignissim dui, in molestie metus feugiat sed.</p></div>
    <div class="pct-label" style="left:216px"><div class="h-gold" style="color:var(--gold-light)">Heading Goes Here</div><p class="lorem">Lorem ipsum dolor sit amet, consectetur adipiscing elit. Vivamus eu dui ex. Curabitur dapibus dignissim dui, in molestie metus feugiat sed.</p></div>
    <div class="pct-label" style="left:372px"><div class="h-ink">Heading Goes Here</div><p class="lorem">Lorem ipsum dolor sit amet, consectetur adipiscing elit. Vivamus eu dui ex. Curabitur dapibus dignissim dui, in molestie metus feugiat sed.</p></div>
    <div class="brand-sm"><span class="dot"></span>TARVEL WORKS</div>
    <div class="copy">Copyright © 2023 Tarvel Works. All rights reserved.</div>
    <div class="pg">9</div>
  </article>

  <article class="slide col-r row5">
    <h2 class="s-title">HEADING GOES HERE</h2>
    <div class="hl-frame"></div>
    <table class="data">
      <colgroup><col style="width:157px"><col style="width:87px"><col style="width:87px"><col style="width:87px"><col style="width:87px"></colgroup>
      <tr><th>Heading Goes Here</th><th class="hl">Heading<br>Goes Here</th><th>Heading<br>Goes Here</th><th>Heading<br>Goes Here</th><th>Heading<br>Goes Here</th></tr>
      <tr><td>Lorem ipsum dolor sit amet</td><td class="hl">23</td><td>12</td><td>78</td><td>78</td></tr>
      <tr><td>Vivamus eu dui ex. Curabitur dapibus</td><td class="hl">45</td><td>56</td><td>12</td><td>76</td></tr>
      <tr><td>Praesent aliquet lorem ex, eu dapibus</td><td class="hl">78</td><td>76</td><td>34</td><td>34</td></tr>
      <tr><td>Duis eget tellus porta, consequat lacus</td><td class="hl">22</td><td>12</td><td>55</td><td>67</td></tr>
      <tr><td>Donec risus orci, gravida sit amet</td><td class="hl">34</td><td>66</td><td>45</td><td>11</td></tr>
      <tr><td>Nunc placerat, arcu nec mattis</td><td class="hl">67</td><td>47</td><td>78</td><td>23</td></tr>
      <tr><td>Nam semper tristique mauris</td><td class="hl">87</td><td>67</td><td>12</td><td>45</td></tr>
    </table>
    <div class="brand-sm"><span class="dot"></span>TARVEL WORKS</div>
    <div class="copy">Copyright © 2023 Tarvel Works. All rights reserved.</div>
    <div class="pg">10</div>
  </article>

  <!-- row 6: contact -->
  <article class="slide contact col-l row6">
    <svg class="cover-art" viewBox="0 0 563 316" role="img" aria-label="Photo: glass office tower seen from below">
      <defs>
        <linearGradient id="goldD" x1="0" y1="1" x2="1" y2="0"><stop offset="0" stop-color="#b9791f"/><stop offset="1" stop-color="#f2ca66"/></linearGradient>
        <linearGradient id="photoD" x1="0" y1="0" x2="1" y2="1"><stop offset="0" stop-color="#dfe4e6"/><stop offset=".5" stop-color="#5f7478"/><stop offset="1" stop-color="#203034"/></linearGradient>
      </defs>
      <path d="M310 0H563V316H330C290 250 250 170 240 115C230 55 262 0 310 0Z" fill="url(#goldD)"/>
      <path d="M395 0H563V316H405C370 255 330 185 318 135C305 75 340 18 395 0Z" fill="url(#photoD)"/>
    </svg>
    <div class="brand"><span class="dot"></span>TARVEL WORKS</div>
    <div class="contact-head">Contact Us</div>
    <ul class="contact-list">
      <li><svg viewBox="0 0 10 10"><path d="M2 1l2 2-1 1.5c.6 1.2 1.3 1.9 2.5 2.5L7 6l2 2-1.5 1.5C4.5 9 1 5.5.5 2.5z" fill="var(--gold)"/></svg>Phone Number Goes Here</li>
      <li><svg viewBox="0 0 10 10"><circle cx="5" cy="5" r="1.8" fill="none" stroke="var(--gold)" stroke-width="1.2"/><path d="M6.8 3.5v2.3c0 1 1.8 1 1.8-.8A3.6 3.6 0 1 0 7 8" fill="none" stroke="var(--gold)" stroke-width="1.2"/></svg>E-Mail Address Goes Here</li>
      <li><svg viewBox="0 0 10 10"><circle cx="5" cy="5" r="4" fill="none" stroke="var(--gold)" stroke-width="1"/><path d="M1 5h8M5 1c2 2.5 2 5.5 0 8M5 1C3 3.5 3 6.5 5 9" fill="none" stroke="var(--gold)" stroke-width=".8"/></svg>URL Address Goes Here</li>
    </ul>
    <div class="cover-copy">Copyright © 2023 Tarvel Works. All rights reserved.</div>
  </article>

  <article class="slide contact col-r row6">
    <svg class="cover-art" viewBox="0 0 563 316" role="img" aria-label="Photo: two people shaking hands in an office">
      <defs>
        <linearGradient id="goldE" x1="0" y1="1" x2="1" y2="0"><stop offset="0" stop-color="#b9791f"/><stop offset="1" stop-color="#f2ca66"/></linearGradient>
        <linearGradient id="photoE" x1="0" y1="0" x2="1" y2="1"><stop offset="0" stop-color="#cfd8e0"/><stop offset=".5" stop-color="#7a8998"/><stop offset="1" stop-color="#2a3544"/></linearGradient>
      </defs>
      <path d="M310 0H563V316H330C290 250 250 170 240 115C230 55 262 0 310 0Z" fill="url(#goldE)"/>
      <path d="M395 0H563V316H405C370 255 330 185 318 135C305 75 340 18 395 0Z" fill="url(#photoE)"/>
    </svg>
    <div class="brand"><span class="dot"></span>TARVEL WORKS</div>
    <div class="contact-head">Contact Us</div>
    <ul class="contact-list">
      <li><svg viewBox="0 0 10 10"><path d="M2 1l2 2-1 1.5c.6 1.2 1.3 1.9 2.5 2.5L7 6l2 2-1.5 1.5C4.5 9 1 5.5.5 2.5z" fill="var(--gold)"/></svg>Phone Number Goes Here</li>
      <li><svg viewBox="0 0 10 10"><circle cx="5" cy="5" r="1.8" fill="none" stroke="var(--gold)" stroke-width="1.2"/><path d="M6.8 3.5v2.3c0 1 1.8 1 1.8-.8A3.6 3.6 0 1 0 7 8" fill="none" stroke="var(--gold)" stroke-width="1.2"/></svg>E-Mail Address Goes Here</li>
      <li><svg viewBox="0 0 10 10"><circle cx="5" cy="5" r="4" fill="none" stroke="var(--gold)" stroke-width="1"/><path d="M1 5h8M5 1c2 2.5 2 5.5 0 8M5 1C3 3.5 3 6.5 5 9" fill="none" stroke="var(--gold)" stroke-width=".8"/></svg>URL Address Goes Here</li>
    </ul>
    <div class="cover-copy">Copyright © 2023 Tarvel Works. All rights reserved.</div>
  </article>

</div>
</body>
</html>
```